KVT Meridale Sales Proposal: Anti-Glare Film

I need a professional and visually engaging PowerPoint presentation designed for a sales pitch on an anti-glare optical film for electronic screens. The presentation should be 10-15 minutes long, with a clean, creative, and modern design.
Key Requirements:
- Strong visual appeal with clear graphics and minimal text.
- Well-structured format including product introduction, benefits, competitive advantages, and market applications.
- Creative elements to make the pitch engaging (icons, infographics, smart animations).
- Consistent, corporate-style theme fitting KVT Meridale’s branding.
- Final slide should include a closing statement and invitation for a Q&A.
Please ensure the design is polished, professional, and captures attention effectively.

```html
<!DOCTYPE html>
<html lang="en">
<head>
<meta charset="utf-8">
<title>KVT Meridale – Anti-Glare Film</title>
<link href="https://fonts.googleapis.com/css2?family=Carlito:wght@400;700&display=swap" rel="stylesheet">
<style>
  :root {
    --page: #ffffff;
    --deep-blue: #1c3cae;
    --mid-blue: #0f2272;
    --night: #050a22;
    --black: #000000;
    --title-blue: #3b8ad6;
    --label-blue: #3f8fd8;
    --product-blue: #0b63b8;
    --cell-grey: #5b5b5b;
    --haze-teal: #3a84aa;
    --gold: #c49300;
    --gold-note: #e6a800;
    --white: #ffffff;
    --badge: rgba(60, 90, 200, 0.55);
  }
  * { box-sizing: border-box; margin: 0; padding: 0; }
  html, body { width: 675px; height: 1200px; overflow: hidden; background: var(--page); }
  body { position: relative; font-family: "Carlito", "Calibri", sans-serif; color: var(--white); }

  .slide {
    position: absolute; left: 61px; width: 556px; height: 313px; overflow: hidden;
    background: linear-gradient(158deg, var(--deep-blue) 0%, var(--mid-blue) 30%, var(--night) 55%, var(--black) 75%);
  }
  .slide--applications { top: 102px; }
  .slide--properties { top: 445px; }
  .slide--qa { top: 804px; }

  .brand-badge {
    position: absolute; left: 23px; top: 13px; width: 149px; height: 25px;
    background: var(--badge); display: flex; align-items: center; gap: 6px; padding-left: 14px;
  }
  .brand-badge .mark { width: 9px; height: 9px; background: var(--white); }
  .brand-badge .name { font-weight: 700; font-size: 8px; color: var(--white); }

  .section-title {
    position: absolute; right: 347px; top: 89px; font-size: 17px; font-weight: 400;
    color: var(--title-blue); white-space: nowrap; line-height: 20px;
  }
  .divider { position: absolute; left: 231px; top: 82px; width: 1px; height: 190px; background: var(--title-blue); opacity: .8; }

  .applications-text { position: absolute; left: 261px; top: 90px; font-size: 9.6px; line-height: 12.5px; }
  .app-visual { position: absolute; left: 306px; top: 128px; width: 133px; height: 161px;
    background: linear-gradient(135deg, #1a22c8 0%, #2d1a8a 45%, #c0427a 70%, #0b0b2a 100%); }
  .app-visual--small { left: 424px; top: 190px; width: 64px; height: 64px;
    background: linear-gradient(150deg, #d8c7a2, #8c7a5c); }

  .properties-title { right: 348px; top: 89px; }
  .properties-rule { position: absolute; left: 59px; top: 111px; width: 184px; height: 1px; background: var(--title-blue); }

  .col-label { position: absolute; font-weight: 700; font-size: 9.5px; color: var(--label-blue); text-align: center; }
  .cell { position: absolute; display: flex; align-items: center; justify-content: center; text-align: center; border-radius: 4px; }
  .cell--product { left: 11px; width: 52px; font-weight: 700; font-size: 5.6px; line-height: 7px; background: var(--product-blue); border: 1px solid #2f7fd0; }
  .cell--product-head { background: var(--white); color: var(--product-blue); font-size: 7.5px; }
  .cell--substrate { left: 70px; width: 81px; height: 21px; font-size: 7.5px; background: var(--cell-grey); border: 1px solid #bdbdbd; }
  .cell--status { left: 159px; width: 88px; height: 26px; font-size: 8px; background: var(--cell-grey); }
  .cell--tt { left: 256px; width: 79px; height: 32px; font-size: 10px; background: var(--cell-grey); }
  .cell--haze { left: 345px; width: 85px; height: 37px; font-size: 10px; background: var(--haze-teal); }
  .cell--spark { left: 442px; width: 87px; height: 43px; font-size: 13px; font-weight: 700; background: var(--gold); }
  .footnote { position: absolute; right: 27px; top: 262px; font-size: 7.5px; color: var(--gold-note); }
</style>
</head>
<body>

<section class="slide slide--applications">
  <div class="brand-badge"><span class="mark"></span><span class="name">KVT Meridale, LLC</span></div>
  <h2 class="section-title">Applications</h2>
  <div class="divider"></div>
  <p class="applications-text">High Resolution Monitor, High-end Note PC,<br>Display for Medical Use</p>
  <div class="app-visual" role="img" aria-label="Photo of a laptop and a high resolution monitor with colourful wallpaper"></div>
  <div class="app-visual app-visual--small" role="img" aria-label="Photo of a medical patient monitor"></div>
</section>

<section class="slide slide--properties">
  <div class="brand-badge"><span class="mark"></span><span class="name">KVT Meridale, LLC</span></div>
  <h2 class="section-title properties-title">Properties</h2>
  <div class="properties-rule"></div>

  <div class="cell cell--product cell--product-head" style="top:137px;height:19px;">Products</div>
  <div class="cell cell--product" style="top:162px;height:20px;">Standard AG</div>
  <div class="cell cell--product" style="top:187px;height:20px;">AG for High-res<br>Conventional</div>
  <div class="cell cell--product" style="top:213px;height:20px;">AG for Super<br>High Resolution</div>

  <div class="col-label" style="left:70px;width:81px;top:142px;">Substrate</div>
  <div class="cell cell--substrate" style="top:161px;">TAC (25,40,60,80μm)</div>
  <div class="cell cell--substrate" style="top:187px;">TAC (25,40,80μm)</div>
  <div class="cell cell--substrate" style="top:213px;">TAC (25,40,60,80μm)</div>

  <div class="col-label" style="left:159px;width:88px;top:134px;">Status</div>
  <div class="cell cell--status" style="top:152px;">MP</div>
  <div class="cell cell--status" style="top:182px;">MP</div>
  <div class="cell cell--status" style="top:213px;">Under development</div>

  <div class="col-label" style="left:256px;width:79px;top:120px;">T.T. (%)</div>
  <div class="cell cell--tt" style="top:139px;">91</div>
  <div class="cell cell--tt" style="top:175px;">91</div>
  <div class="cell cell--tt" style="top:212px;">91</div>

  <div class="col-label" style="left:345px;width:85px;top:110px;">Haze (%)</div>
  <div class="cell cell--haze" style="top:127px;">25</div>
  <div class="cell cell--haze" style="top:169px;">40</div>
  <div class="cell cell--haze" style="top:210px;">40</div>

  <div class="col-label" style="left:432px;width:107px;top:92px;">Anti-sparking (σ)</div>
  <div class="cell cell--spark" style="top:110px;">28</div>
  <div class="cell cell--spark" style="top:161px;">17</div>
  <div class="cell cell--spark" style="top:210px;">13</div>

  <p class="footnote">*smaller is better</p>
</section>

<section class="slide slide--qa">
  <div class="brand-badge"><span class="mark"></span><span class="name">KVT Meridale, LLC</span></div>
  <h2 class="section-title">Q&amp;A</h2>
  <div class="divider"></div>
</section>

</body>
</html>
```